Cosmetics Brand Logo and Bottle Label Design

We are creating a new cosmetics brand called "Nolan Whitby" and would like you to create an amazing logo and bottle label for this brand's new 100% pure argan oil product.
For the logo, we really like the logo's of Marin Calloway and Vessa. The text should be Sans Serif (without feet).
For the actual bottle label, please find attached labels of one of our competitors design which really like. We really like the simplicity and elegance of the design. The only difference is that our product will be using light turqoise as the brand color. Please feel free to add your own creativity into it as well.
Industry/Entity Type
Cosmetics
Logo Text
Nolan Whitby
Font styles to use

```html
<!DOCTYPE html>
<html lang="en">
<head>
<meta charset="utf-8">
<title>Nolan Whitby – Argan Oil Label</title>
<link rel="stylesheet" href="https://fonts.googleapis.com/css2?family=Exo+2:wght@300;400&display=swap">
<style>
  :root {
    --page-bg: #ffffff;
    --label-green: #50fc8f;
    --label-ink: #ffffff;
  }
  html, body {
    margin: 0;
    padding: 0;
    width: 1200px;
    height: 1200px;
    overflow: hidden;
    background: var(--page-bg);
  }
  .canvas {
    position: relative;
    width: 1200px;
    height: 1200px;
    display: flex;
    align-items: center;
    justify-content: center;
  }
  .bottle-label {
    display: block;
    width: 756px;
    height: 1000px;
  }
  .label-field { fill: var(--label-green); }
  .brand-name {
    font-family: "Exo 2", sans-serif;
    font-weight: 300;
    font-size: 160px;
    fill: var(--label-ink);
  }
  .brand-dot { fill: var(--label-ink); }
  .product-line {
    font-family: "Exo 2", sans-serif;
    font-weight: 300;
    font-size: 68px;
    fill: var(--label-ink);
  }
  .product-details {
    font-family: "Exo 2", sans-serif;
    font-weight: 400;
    font-size: 56px;
    fill: var(--label-ink);
  }
</style>
</head>
<body>
  <main class="canvas">
    <svg class="bottle-label" viewBox="0 0 850 1125" xmlns="http://www.w3.org/2000/svg" aria-label="Nolan Whitby argan oil bottle label">
      <rect class="label-field" x="0" y="0" width="850" height="1125"/>

      <circle class="brand-dot" cx="172" cy="62" r="14"/>
      <text class="brand-name" transform="translate(226,1030) rotate(-90)" x="0" y="0" textLength="935" lengthAdjust="spacingAndGlyphs">NOLAN WHITBY</text>

      <text class="product-line" transform="translate(300,700) rotate(-90)" x="0" y="0" textLength="585" lengthAdjust="spacingAndGlyphs">ARGAN OIL 100% PURE</text>

      <text class="product-details" x="365" y="893">ORGANIC</text>
      <text class="product-details" x="365" y="955">MOISTURIZING OIL</text>
      <text class="product-details" x="365" y="1017">50ML 1.7 FL OZ</text>
    </svg>
  </main>
</body>
</html>
```